Small business updating business cards

We have already updated our logo via Pixel Forum and downloaded it (hopefully) for you to use. Now an updated set of business cards for Neil Pollard and Stuart Pollard are also needed... we are also hoping that a copy of our outdated business card designs have uploaded successfully as Microsoft Publisher files. Our Strength Through Unity motto has died a slow death so we are hoping to remove it (and other superfluous lingo if the graphic covers the idea) and instead opt for a fancy graphic (?) on the second side of the card that really reflects our desire to obtain product / haulage from Road Transport / Yard Operators and convert legs of their haulage to rail freight where profitable (bulk haulage / containterised etc). Can you help us look larger, bolder and more robust than we really are (two man show)?
Target Market(s)
Transport Industry
Industry/Entity Type
Business
Contact Information for Business Card
Card details for both N Pollard and S Pollard have been uploaded on the publisher files
Colors
Designer to choose colors to be used in the design.
Requirements
Must have
- Similar theme both sides of card
Should not have
- Black on one side white on the other

```html
<!DOCTYPE html>
<html lang="en">
<head>
<meta charset="utf-8">
<title>Linkrail Business Cards</title>
<link rel="stylesheet" href="https://fonts.googleapis.com/css2?family=Open+Sans:wght@400;600;700&display=swap">
<style>
  :root {
    --backdrop: #7dd5c5;
    --card-white: #f6f6f4;
    --brand-green: #5d8f58;
    --brand-teal: #3a8787;
    --brand-olive: #6a9a5a;
    --ink-white: #ffffff;
    --shadow: rgba(30, 80, 70, 0.25);
  }
  html, body {
    margin: 0;
    padding: 0;
    width: 1200px;
    height: 1200px;
    overflow: hidden;
    background: var(--backdrop);
    font-family: "Open Sans", Arial, sans-serif;
  }
  .card-sheet {
    width: 1200px;
    height: 1200px;
    display: flex;
    flex-direction: column;
    align-items: center;
    justify-content: center;
    gap: 80px;
  }
  .business-card {
    width: 735px;
    height: 420px;
    display: block;
    box-shadow: 0 18px 30px var(--shadow);
  }
  .brand-name {
    font-family: "Open Sans", Arial, sans-serif;
    font-weight: 700;
    fill: var(--brand-green);
  }
  .person-name { font-weight: 400; fill: var(--ink-white); }
  .person-role { font-weight: 400; fill: var(--ink-white); }
  .contact-line { font-weight: 400; fill: var(--ink-white); }
  .band-text { font-weight: 400; fill: var(--ink-white); }
  .icon-ring { fill: none; stroke: var(--ink-white); stroke-width: 1.6; }
  .icon-glyph { fill: none; stroke: var(--ink-white); stroke-width: 1.4; stroke-linecap: round; }
</style>
</head>
<body>
<main class="card-sheet">

  <!-- Card front -->
  <svg class="business-card card-front" viewBox="0 0 735 420" xmlns="http://www.w3.org/2000/svg" aria-label="Linkrail business card front">
    <defs>
      <linearGradient id="end-fill" x1="0" y1="0" x2="1" y2="1">
        <stop offset="0" stop-color="var(--brand-olive)"/>
        <stop offset="0.55" stop-color="var(--brand-teal)"/>
        <stop offset="1" stop-color="var(--brand-green)"/>
      </linearGradient>
    </defs>
    <rect class="card-base" width="735" height="420" fill="var(--card-white)"/>
    <path class="end-curve end-curve-left" d="M0,0 H150 Q40,210 150,420 H0 Z" fill="url(#end-fill)"/>
    <path class="end-curve end-curve-right" d="M735,0 H585 Q695,210 585,420 H735 Z" fill="url(#end-fill)"/>
    <circle cx="238" cy="212" r="12" fill="var(--brand-teal)"/>
    <text class="brand-name" x="382" y="230" font-size="58" text-anchor="middle">Linkrail</text>
  </svg>

  <!-- Card back -->
  <svg class="business-card card-back" viewBox="0 0 735 420" xmlns="http://www.w3.org/2000/svg" aria-label="Linkrail business card for Neil Pollard">
    <defs>
      <linearGradient id="panel-fill" x1="0" y1="0" x2="1" y2="1">
        <stop offset="0" stop-color="var(--brand-teal)"/>
        <stop offset="0.5" stop-color="var(--brand-olive)"/>
        <stop offset="1" stop-color="var(--brand-teal)"/>
      </linearGradient>
      <clipPath id="card-clip"><rect width="735" height="420"/></clipPath>
    </defs>
    <g clip-path="url(#card-clip)">
      <rect class="card-base" width="735" height="420" fill="var(--card-white)"/>
      <path class="info-panel" d="M0,0 H440 C590,90 590,330 420,420 H0 Z" fill="url(#panel-fill)"/>
      <rect class="tagline-band" x="398" y="300" width="360" height="78" rx="14" fill="var(--brand-green)"/>

      <text class="person-name" x="150" y="82" font-size="42">Neil Pollard</text>
      <text class="person-role" x="206" y="116" font-size="22">Director</text>

      <g class="contact-list" font-size="17">
        <g class="contact-phone">
          <circle class="icon-ring" cx="40" cy="168" r="11"/>
          <path class="icon-glyph" d="M35,162 q0,10 10,12 l1,-3 -3,-2 -2,2 q-3,-2 -4,-5 l2,-2 -2,-3 z"/>
          <text class="contact-line" x="62" y="174">0400 123 987</text>
        </g>
        <g class="contact-email">
          <circle class="icon-ring" cx="40" cy="202" r="11"/>
          <text x="40" y="208" font-size="15" text-anchor="middle" fill="var(--ink-white)">@</text>
          <text class="contact-line" x="62" y="208">pollardn@linkrail.com.au</text>
        </g>
        <g class="contact-web">
          <circle class="icon-ring" cx="40" cy="236" r="11"/>
          <ellipse class="icon-glyph" cx="40" cy="236" rx="4.5" ry="10"/>
          <line class="icon-glyph" x1="30" y1="236" x2="50" y2="236"/>
          <text class="contact-line" x="62" y="242">www.linkrail.com.au</text>
        </g>
        <g class="contact-address">
          <text class="contact-line" x="62" y="282">14 Harbour Lane</text>
          <text class="contact-line" x="62" y="304">Fernvale NSW 2290</text>
        </g>
      </g>

      <g class="brand-lockup">
        <circle cx="580" cy="170" r="8" fill="var(--brand-teal)"/>
        <text class="brand-name" x="594" y="182" font-size="33">Linkrail</text>
      </g>

      <g class="band-text" font-size="17">
        <text x="438" y="328">Strategic Alliance Partners</text>
        <text x="438" y="349">Providing Logistical</text>
        <text x="438" y="370">Freight Solutions</text>
      </g>
    </g>
  </svg>

</main>
</body>
</html>
```